Business Card Design Project- Removalist

I would like to surprise my husband to be with a different type of wedding present. His brother (who he owned a removalist business with) suddenly passed away from cancer recently and he has changed his business name to 'RTB' (which stands for Raising Tom Bright; but the full name doesn't need to be on the business card as it is more of a personal business name). To celebrate the new business I would like to get him some business cards made.
I would like the business name to be listed as 'RTB' and somewhere on the card I would like 'Sydney wide removals and relocation services'. I would like it to be obvious from the front of the card that it is a removalist business card. If a truck or some other feature that makes it look like a removalist business card could added it would be appreciated.
I don't mind what colours are used, but I would like the colour blue to feature somewhere in the design. It can be bright and fun, which is how Tom was.
I will also need the company's email address and phone number listed
The email address is: rtbremovals@quillpost.example
The contact number is: 0417 282 934
I don't need a contact name listed on the card, but perhaps 'Owned and operated by the Pendleworth family' could be added near the contact details in small font.
Thank you very much for considering this project!
Kind regards,
Fiona
Updates
Could you please change the mobile contact number to 0417 282 934. This is the only contact phone number required on the card now.
Thank you!

```html
<!DOCTYPE html>
<html lang="en">
<head>
<meta charset="utf-8">
<title>RTB Removals – Business Cards</title>
<link rel="stylesheet" href="https://fonts.googleapis.com/css2?family=Roboto+Condensed:wght@400;700&family=Arimo:wght@400&display=swap">
<style>
  :root {
    --navy: #28338c;
    --blue: #1b8ad3;
    --sky: #4db3e6;
    --green: #8dc63f;
    --paper: #ffffff;
    --backdrop: #f4f5f7;
    --card-shadow: 0 6px 22px rgba(20, 30, 70, 0.16);
  }
  * { box-sizing: border-box; margin: 0; padding: 0; }
  html, body {
    width: 1200px;
    height: 1085px;
    overflow: hidden;
    background: var(--backdrop);
  }
  .sheet {
    position: relative;
    width: 1200px;
    height: 1085px;
  }
  .card {
    position: absolute;
    width: 640px;
    height: 388px;
    background: var(--paper);
    box-shadow: var(--card-shadow);
    overflow: hidden;
    font-family: "Roboto Condensed", "Arial Narrow", sans-serif;
  }
  .card--light { left: 90px; top: 90px; }
  .card--banded { left: 470px; top: 600px; }

  .tagline {
    position: absolute;
    left: 34px;
    top: 24px;
    font-weight: 700;
    font-size: 29px;
    letter-spacing: -0.2px;
    color: var(--blue);
    white-space: nowrap;
  }
  .tagline__city { color: var(--navy); }
  .owner-note {
    position: absolute;
    right: 30px;
    top: 60px;
    font-family: "Arimo", Arial, sans-serif;
    font-size: 12.5px;
    color: var(--navy);
    letter-spacing: 0.3px;
  }

  .brand {
    position: absolute;
    left: 34px;
    top: 82px;
    width: 572px;
    height: 188px;
    display: flex;
    align-items: center;
    justify-content: center;
    gap: 26px;
  }
  .brand__dot {
    width: 46px;
    height: 46px;
    border-radius: 50%;
    background: var(--blue);
  }
  .brand__name {
    font-weight: 700;
    font-size: 190px;
    line-height: 1;
    color: var(--blue);
    letter-spacing: 2px;
  }

  .contact-line {
    position: absolute;
    left: 34px;
    top: 284px;
    font-weight: 700;
    font-size: 46px;
    line-height: 1;
    white-space: nowrap;
  }
  .contact-line__cta { color: var(--navy); margin-right: 10px; }
  .contact-line__phone { color: var(--blue); }
  .email {
    position: absolute;
    right: 32px;
    top: 338px;
    font-family: "Arimo", Arial, sans-serif;
    font-size: 17px;
    color: var(--blue);
  }

  .band {
    position: absolute;
    left: 0;
    bottom: 0;
    width: 100%;
    height: 118px;
    background: var(--navy);
  }
  .band .contact-line { top: 22px; font-size: 54px; }
  .band .contact-line__cta { color: var(--green); margin-right: 18px; }
  .band .contact-line__phone { color: var(--paper); }
  .band .email { top: 84px; color: var(--paper); font-size: 16px; }
  .card--banded .brand { top: 78px; height: 164px; }
  .card--banded .brand__name { font-size: 170px; }
</style>
</head>
<body>
<main class="sheet">

  <section class="card card--light" aria-label="Business card, white layout">
    <p class="tagline"><span class="tagline__city">SYDNEY</span> WIDE REMOVALS &amp; RELOCATION SERVICES</p>
    <p class="owner-note">Owned and operated by the PENDLEWORTH family</p>
    <div class="brand">
      <span class="brand__dot"></span>
      <span class="brand__name">RTB</span>
    </div>
    <p class="contact-line"><span class="contact-line__cta">CALL US!</span><span class="contact-line__phone">0417 282 934</span></p>
    <p class="email">email: rtbremovals@quillpost.example</p>
  </section>

  <section class="card card--banded" aria-label="Business card, banded layout">
    <p class="tagline"><span class="tagline__city">SYDNEY</span> WIDE REMOVALS &amp; RELOCATION SERVICES</p>
    <p class="owner-note">Owned and operated by the PENDLEWORTH family</p>
    <div class="brand">
      <span class="brand__dot"></span>
      <span class="brand__name">RTB</span>
    </div>
    <div class="band">
      <p class="contact-line"><span class="contact-line__cta">CALL US!</span><span class="contact-line__phone">0417 282 934</span></p>
      <p class="email">rtbremovals@quillpost.example</p>
    </div>
  </section>

</main>
</body>
</html>
```